Food Trade Show Advertisement

One full-page advertisement sent as a high-resolution .pdf file that is 11.125" w x 14.25" h

Details on the the wording and pictures will be provided
The to include:
Company logo, product photos (to be supplied), wording (to be supplied), Booth number (to be supplied)
Colors - hot pink
Attached is the guidelines for the advertisement

```html
<!DOCTYPE html>
<html lang="en">
<head>
<meta charset="utf-8">
<title>Bellbean – Trade Show Advertisement</title>
<link rel="stylesheet" href="https://fonts.googleapis.com/css2?family=Bebas+Neue&family=Montserrat:wght@400;500&display=swap">
<style>
  :root {
    --hot-pink: #e8288a;
    --deep-pink: #d41a78;
    --blush: #f4dbe2;
    --blush-deep: #ebcbd4;
    --grain: #e6cf9a;
    --ink: #1d1d1d;
    --white: #ffffff;
  }
  * { margin: 0; padding: 0; box-sizing: border-box; }
  html, body { width: 937px; height: 1200px; overflow: hidden; background: var(--white); }
  .ad {
    position: relative;
    width: 937px;
    height: 1200px;
    overflow: hidden;
    background: var(--white);
    font-family: "Montserrat", sans-serif;
    color: var(--ink);
  }
  .hero-art { position: absolute; left: 0; top: 0; width: 937px; height: 780px; }
  .brand {
    position: absolute;
    left: 38px;
    top: 58px;
    font-family: "Bebas Neue", sans-serif;
    font-size: 112px;
    line-height: 1;
    letter-spacing: 2px;
    color: var(--hot-pink);
  }
  .booth {
    position: absolute;
    left: 733px;
    top: 0;
    width: 164px;
    height: 213px;
    background: var(--white);
    border-radius: 0 0 36px 36px;
    text-align: center;
    font-family: "Bebas Neue", sans-serif;
    color: var(--hot-pink);
  }
  .booth-label { display: block; font-size: 42px; line-height: 1; margin-top: 30px; letter-spacing: 1px; }
  .booth-sub { display: block; font-size: 30px; line-height: 0.9; letter-spacing: 1px; }
  .booth-number { display: block; font-size: 100px; line-height: 0.9; margin-top: 2px; letter-spacing: 2px; }
  .headline {
    position: absolute;
    left: 36px;
    top: 756px;
    font-family: "Bebas Neue", sans-serif;
    font-weight: 400;
    font-size: 60px;
    line-height: 55px;
    color: var(--hot-pink);
    letter-spacing: 0.5px;
  }
  .phone-bar {
    position: absolute;
    left: 628px;
    top: 806px;
    width: 309px;
    height: 49px;
    background: var(--hot-pink);
    font-family: "Bebas Neue", sans-serif;
    font-size: 38px;
    line-height: 51px;
    letter-spacing: 3px;
    color: var(--white);
    padding-left: 26px;
  }
  .phone-icon { position: absolute; left: 552px; top: 788px; width: 86px; height: 86px; }
  .body-copy {
    position: absolute;
    left: 37px;
    top: 880px;
    width: 860px;
    font-size: 14.6px;
    line-height: 19.6px;
    text-align: justify;
  }
  .footer-wave { position: absolute; left: 0; top: 1050px; width: 937px; height: 150px; }
  .social { position: absolute; top: 1112px; left: 0; width: 937px; height: 16px; }
  .social-dot {
    position: absolute;
    width: 14px;
    height: 14px;
    border-radius: 50%;
    background: var(--white);
  }
  .footer-copy {
    position: absolute;
    left: 50px;
    top: 1138px;
    width: 852px;
    font-size: 11px;
    line-height: 18px;
    color: var(--white);
  }
</style>
</head>
<body>
<main class="ad">
  <svg class="hero-art" viewBox="0 0 937 780" aria-hidden="false">
    <defs>
      <linearGradient id="backdropTone" x1="0" y1="0" x2="1" y2="1">
        <stop offset="0" stop-color="#f6e1e6"/>
        <stop offset="0.55" stop-color="#f1d6dd"/>
        <stop offset="1" stop-color="#ebcbd3"/>
      </linearGradient>
      <radialGradient id="flourTone" cx="0.5" cy="0.55" r="0.6">
        <stop offset="0" stop-color="#efdcae"/>
        <stop offset="1" stop-color="#d9d6d2"/>
      </radialGradient>
      <radialGradient id="chunkTone" cx="0.5" cy="0.55" r="0.6">
        <stop offset="0" stop-color="#dcc06a"/>
        <stop offset="1" stop-color="#f2ede0"/>
      </radialGradient>
    </defs>
    <g role="img" aria-label="Photo of two baguettes and wheat stalks on a soft pink surface">
      <path d="M188,0 H937 V572 C880,596 760,612 640,606 C500,598 360,575 280,505 C215,445 192,360 188,270 Z" fill="url(#backdropTone)"/>
    </g>
    <g role="img" aria-label="Photo of faba bean flour spilling from a grey cloth bag">
      <circle cx="275" cy="425" r="124" fill="var(--white)"/>
      <circle cx="275" cy="425" r="114" fill="url(#flourTone)"/>
    </g>
    <g role="img" aria-label="Photo of textured faba bean protein chunks">
      <circle cx="463" cy="640" r="120" fill="var(--white)"/>
      <circle cx="463" cy="640" r="110" fill="url(#chunkTone)"/>
    </g>
    <g role="img" aria-label="Photo of a pile of faba bean flour on a grey cloth">
      <circle cx="757" cy="668" r="124" fill="var(--white)"/>
      <circle cx="757" cy="668" r="114" fill="url(#flourTone)"/>
    </g>
  </svg>

  <div class="brand">Bellbean</div>

  <div class="booth">
    <span class="booth-label">Booth</span>
    <span class="booth-sub">Number</span>
    <span class="booth-number">00</span>
  </div>

  <h1 class="headline">Add your title<br>and tagline here</h1>

  <div class="phone-bar">+123 456 78 90</div>
  <svg class="phone-icon" viewBox="0 0 86 86" aria-label="Phone">
    <circle cx="43" cy="43" r="43" fill="var(--hot-pink)"/>
    <circle cx="43" cy="43" r="33" fill="none" stroke="var(--white)" stroke-width="4"/>
    <path d="M31,28 l6,-3 l5,10 l-4,3 c2,5 5,8 10,10 l3,-4 l10,5 l-3,6 c-14,1 -28,-13 -27,-27 z" fill="var(--white)"/>
    <path d="M46,30 a10,10 0 0 1 10,10" fill="none" stroke="var(--white)" stroke-width="2.6" stroke-linecap="round"/>
    <path d="M46,23 a17,17 0 0 1 17,17" fill="none" stroke="var(--white)" stroke-width="2.6" stroke-linecap="round"/>
  </svg>

  <div class="body-copy">
    <p>Lorem ipsum dolor sit amet, consectetur adipiscing elit, sed do eiusmod tempor incididunt ut labore et dolore magna aliqua. Quis ipsum suspendisse ultrices gravida. Risus commodo viverra maecenas accumsan lacus vel facilisis.</p>
    <p>Lorem ipsum dolor sit amet, consectetur adipiscing elit, sed do eiusmod tempor incididunt ut labore et dolore magna aliqua. Quis ipsum suspendisse ultrices gravida. Risus commodo viverra maecenas accumsan lacus vel facilisis. Lorem ipsum dolor sit amet, consectetur adipiscing elit, sed do eiusmod tempor incididunt ut labore et dolore magna aliqua. Quis ipsum suspendisse ultrices gravida. Risus</p>
  </div>

  <svg class="footer-wave" viewBox="0 0 937 150" preserveAspectRatio="none" aria-hidden="true">
    <defs>
      <linearGradient id="footerTone" x1="0" y1="0" x2="1" y2="0">
        <stop offset="0" stop-color="var(--hot-pink)"/>
        <stop offset="1" stop-color="var(--deep-pink)"/>
      </linearGradient>
    </defs>
    <path d="M0,12 C150,4 300,14 470,22 C640,30 780,18 937,6 V150 H0 Z" fill="url(#footerTone)"/>
    <path d="M0,32 C200,18 420,40 620,34 C760,30 850,30 890,36" fill="none" stroke="var(--white)" stroke-width="3" opacity="0.8"/>
  </svg>

  <div class="social" aria-label="Social media">
    <span class="social-dot" style="left:85px"></span>
    <span class="social-dot" style="left:233px"></span>
    <span class="social-dot" style="left:379px"></span>
  </div>

  <p class="footer-copy">Lorem ipsum dolor sit amet, consectetur adipiscing elit, sed do eiusmod tempor incididunt ut labore et dolore magna aliqua. Quis ipsum suspendisse ultrices gravida. Risus commodo viverra maecenas accumsan lacus vel facilisis.</p>
</main>
</body>
</html>
```